IT Consultancy Needs Daring Webpage (uncoded)

We are looking for a web page for a small IT firm, Larch Systems. We provide remote IT services, website development and IT consultancy. We are looking for a website that is a bit unique and will look both professional and cutting edge.

We are mainly targeting high cash flow small businesses.
Feel free to play with our yellow/blue theme. We where aiming for similar colours to movie posters i.e the Calder Protocol, http://lnk.qorvix.com/t3WmK. Think metallic, flashy and classy like a colourful Zuno.
Updates

We have a website but it is very poor and we would prefer if you did not use it for inspiration.

We quite like this design http://browse.pelmarsketch.com/designs/web/?order=24&offset=24#/k7r9fx2

The three cornerstones of our business are Consult, Support and E-Marketing

other designs are welcome as well (different from the the link above)

Target Market(s)

Small Businesses

Industry/Entity Type

Movie

Requirements
Must have
• Space for Home, Services, Contact and Blog menu bars.

Our logo is ok, you are welcome to adjust it a little to meet your needs.

While we appreciate most websites have a dense middle ground for navigation panels, we would like the most important buttons highlighted as well as a slightly interesting background for example, instead of a plain colour background, a slight hint of a pattern or image.
Should not have
• Should not have a banner.

```html
<!DOCTYPE html>
<html lang="en">
<head>
<meta charset="utf-8">
<title>Larch Systems — Remote IT Services</title>
<link rel="stylesheet" href="https://fonts.googleapis.com/css2?family=Rosarivo&family=Cinzel:wght@400&family=Arimo:wght@400;700&display=swap">
<style>
  :root {
    --black: #000;
    --white: #fff;
    --gold-light: #f8d21a;
    --gold-dark: #c99a06;
    --blue-deep: #0c5a92;
    --blue-mid: #2a7fb8;
    --sky-light: #b6e6f5;
    --sky-mid: #5cc6ec;
    --grey-panel-top: #ececec;
    --grey-panel-bottom: #c9c9c9;
    --grey-box-top: #f7f7f7;
    --grey-box-bottom: #e4e4e4;
    --sun-light: #ffe27a;
    --sun-mid: #ffcb3a;
    --text: #111;
    --text-soft: #444;
    --frame: #f2c21a;
    --serif: "Rosarivo", Georgia, serif;
    --caps: "Cinzel", Georgia, serif;
    --sans: "Arimo", Arial, sans-serif;
  }
  * { box-sizing: border-box; margin: 0; padding: 0; }
  html, body { width: 1188px; height: 1200px; overflow: hidden; background: var(--black); }
  .stage {
    position: relative; width: 1000px; height: 1010px;
    transform: scale(1.188); transform-origin: 0 0;
    background: var(--black); font-family: var(--sans); color: var(--text);
  }
  .abs { position: absolute; }

  /* Top navigation */
  .top-nav {
    left: 177px; top: 30px; width: 823px; height: 48px;
    border-radius: 16px 0 0 0;
    background: linear-gradient(var(--gold-light), var(--gold-dark));
  }
  .top-nav .tab-active {
    left: 90px; top: 0; width: 116px; height: 48px;
    background: linear-gradient(#e3f1fa, #9dcbe6);
  }
  .top-nav .tab-active::before {
    content: ""; position: absolute; left: 48px; top: 0;
    border-left: 10px solid transparent; border-right: 10px solid transparent;
    border-top: 10px solid var(--black);
  }
  .nav-link {
    position: absolute; top: 14px; transform: translateX(-50%);
    font-family: var(--serif); font-size: 17px; color: var(--text); white-space: nowrap;
  }

  /* Banner */
  .banner {
    left: 0; top: 78px; width: 1000px; height: 150px;
    background: linear-gradient(90deg, var(--blue-deep) 0%, #1a6aa4 40%, #3c86bb 55%, #8db6d4 65%);
  }
  .banner-photo {
    left: 540px; top: 0; width: 460px; height: 150px;
    background:
      radial-gradient(ellipse 120px 90px at 70% 40%, rgba(255,255,255,.9), rgba(255,255,255,0)),
      linear-gradient(90deg, rgba(141,182,212,0) 0%, #c4d8e8 25%, #e8f0f6 50%, #d2dce4 75%, #b9c7d3 100%);
  }
  .tagline {
    left: 95px; top: 56px; color: var(--white);
    font-family: var(--caps); font-size: 18px; line-height: 29px; letter-spacing: .3px;
  }

  /* Brand name */
  .brand {
    left: 52px; top: 34px;
    font-family: var(--serif); font-size: 36px; line-height: 40px; color: var(--gold-light);
  }

  /* Main page */
  .page {
    left: 22px; top: 228px; width: 955px; height: 782px;
    background: var(--white);
    border-left: 3px solid var(--frame); border-right: 3px solid var(--frame);
  }
  .welcome-title { left: 50px; top: 240px; font-family: var(--serif); font-size: 24px; font-weight: 400; }
  .welcome-text {
    left: 50px; top: 276px; width: 607px;
    font-size: 12.6px; line-height: 24px; text-align: justify;
  }
  .welcome-photo {
    left: 678px; top: 275px; width: 281px; height: 155px;
    border: 3px solid var(--frame);
    background: linear-gradient(180deg, #ffffff 0%, #f3f1ee 55%, #d9cdbb 100%);
  }

  /* Service boxes */
  .service {
    top: 457px; width: 298px; height: 205px; border-radius: 10px;
    border: 1px solid rgba(0,0,0,.15);
  }
  .service.consult { left: 39px; background: linear-gradient(var(--sky-light), var(--sky-mid)); border-color: #4bb4dc; }
  .service.support { left: 350px; background: linear-gradient(var(--grey-box-top), var(--grey-box-bottom)); border-color: #c8c8c8; }
  .service.marketing { left: 662px; background: linear-gradient(var(--sun-light), var(--sun-mid)); border-color: #d9a82a; }
  .service h2 {
    position: absolute; left: 19px; top: 6px;
    font-family: var(--serif); font-weight: 400; font-size: 24px; white-space: nowrap;
  }
  .service.marketing h2 { left: 16px; }
  .service p {
    position: absolute; left: 19px; top: 57px; width: 247px;
    font-size: 12.6px; line-height: 24px; text-align: justify;
  }
  .service.marketing p { left: 29px; top: 54px; }
  .read-more {
    position: absolute; right: 25px; bottom: -9px; width: 116px; height: 22px;
    border-radius: 11px; border: 1px solid #999;
    background: linear-gradient(#fafafa, #c9c9c9);
    font-size: 12px; line-height: 20px; text-align: center; color: var(--text);
  }

  /* Lower panel */
  .lower {
    left: 25px; top: 683px; width: 950px; height: 252px;
    background: linear-gradient(var(--grey-panel-top), var(--grey-panel-bottom));
  }
  .section-title { font-family: var(--serif); font-size: 24px; font-weight: 400; white-space: nowrap; }
  .centered { transform: translateX(-50%); }

  .news-item { left: 78px; width: 260px; height: 50px; }
  .news-date {
    position: absolute; left: 0; top: 0; width: 50px; height: 50px; border-radius: 50%;
    background: radial-gradient(circle at 50% 30%, #7fd8f6, #1ea6dd);
    border: 1px solid #1189bd; text-align: center; color: #0b2a3a;
  }
  .news-date .day { display: block; margin-top: 12px; font-family: var(--serif); font-size: 16px; line-height: 16px; }
  .news-date .month { display: block; font-size: 8px; }
  .news-text {
    position: absolute; left: 61px; top: 1px; width: 180px;
    font-size: 11.5px; font-weight: 700; line-height: 15px; color: var(--text-soft);
  }

  .field {
    border-radius: 4px; border: 1px solid #d2d2d2;
    background: linear-gradient(#e4e4e4, #f2f2f2);
    box-shadow: 0 1px 2px rgba(0,0,0,.25);
  }
  .btn-dark {
    border-radius: 5px; background: linear-gradient(#5a5a5a, #050505);
    color: var(--white); font-size: 14px; font-weight: 400; text-align: center; line-height: 23px;
  }
  .social { top: 878px; width: 27px; height: 27px; border-radius: 4px; }

  /* Footer */
  .footer-nav {
    left: 17px; top: 935px; width: 971px; height: 34px; border-radius: 10px;
    background: linear-gradient(var(--gold-light), var(--gold-dark));
  }
  .footer-nav .nav-link { top: 6px; color: var(--white); }
  .copyright { left: 500px; top: 981px; font-size: 12px; white-space: nowrap; }
</style>
</head>
<body>
<div class="stage">

  <nav class="top-nav abs">
    <span class="tab-active abs"></span>
    <span class="nav-link" style="left:150px">Home</span>
    <span class="nav-link" style="left:286px">Services</span>
    <span class="nav-link" style="left:436px">Support</span>
    <span class="nav-link" style="left:562px">Blog</span>
    <span class="nav-link" style="left:686px">Contact</span>
  </nav>

  <header class="banner abs">
    <div class="banner-photo abs" role="img" aria-label="Photo of a smiling office team gathered around a computer monitor in a bright office"></div>
    <p class="tagline abs">Remote IT services<br>Website development and IT consultancy.</p>
  </header>

  <div class="brand abs">Larch</div>

  <main class="page abs"></main>

  <h1 class="welcome-title abs">Welcome to Our Website</h1>
  <p class="welcome-text abs">Lorem Ipsum is simply dummy text of the printing and typesetting industry. Lorem Ipsum has been the industry's standard dummy text ever since the 1500s, when an unknown printer took a galley of type and scrambled it to make a type specimen book. It has survived not only five centuries, but also the leap into electronic typesetting, remaining essentially unchanged<br>It was popularised in the 1960s with the release of Letraset sheets containing Lorem Ipsum passages, and more recently with desktop publishing software like Aldus PageMaker including versions of Lorem Ipsum.</p>
  <div class="welcome-photo abs" role="img" aria-label="Photo of two businessmen in an office, one seated at a laptop"></div>

  <section class="service consult abs">
    <h2>Consult</h2>
    <p>There are many variations of passages of Lorem Ipsum available, but the majority have suffered alteration in some form, by injected humour, or randomised words which don't look even slightly believable</p>
    <span class="read-more" style="bottom:-9px">Read more...</span>
  </section>
  <section class="service support abs">
    <h2>Support</h2>
    <p>There are many variations of passages of Lorem Ipsum available, but the majority have suffered alteration in some form, by injected humour, or randomised words which don't look even slightly believable</p>
    <span class="read-more" style="bottom:-13px">Read more...</span>
  </section>
  <section class="service marketing abs">
    <h2>E-Marketing</h2>
    <p>There are many variations of passages of Lorem Ipsum available, but the majority have suffered alteration in some form, by injected humour, or randomised words which don't look even slightly believable</p>
    <span class="read-more" style="bottom:-12px">Read more...</span>
  </section>

  <div class="lower abs"></div>

  <h3 class="section-title abs" style="left:78px;top:689px">Latest News</h3>
  <div class="news-item abs" style="top:741px">
    <span class="news-date"><span class="day">02</span><span class="month">APR</span></span>
    <p class="news-text">Lorem Ipsum is simply dummy text of the printing and typeset-ting industry.</p>
  </div>
  <div class="news-item abs" style="top:804px">
    <span class="news-date"><span class="day">02</span><span class="month">APR</span></span>
    <p class="news-text" style="left:64px">Lorem Ipsum is simply dummy text of the printing and typeset-ting industry.</p>
  </div>
  <div class="news-item abs" style="top:867px">
    <span class="news-date"><span class="day">02</span><span class="month">APR</span></span>
    <p class="news-text" style="left:64px">Lorem Ipsum is simply dummy text of the printing and typeset-ting industry.</p>
  </div>

  <h3 class="section-title abs centered" style="left:500px;top:697px">News Letter</h3>
  <div class="field abs" style="left:403px;top:744px;width:178px;height:28px"></div>
  <div class="btn-dark abs" style="left:441px;top:786px;width:107px;height:24px">Subscribe</div>

  <h3 class="section-title abs centered" style="left:513px;top:834px">Socially Connect</h3>
  <span class="social abs" style="left:430px;background:#3b5a9a" role="img" aria-label="Social network link"></span>
  <span class="social abs" style="left:462px;background:#4fb8e8" role="img" aria-label="Social network link"></span>
  <span class="social abs" style="left:494px;background:#f08a24" role="img" aria-label="News feed link"></span>
  <span class="social abs" style="left:526px;background:#f4f4f4" role="img" aria-label="Photo sharing link"></span>

  <h3 class="section-title abs centered" style="left:795px;top:691px">Contact</h3>
  <div class="field abs" style="left:712px;top:734px;width:178px;height:28px"></div>
  <div class="field abs" style="left:712px;top:773px;width:178px;height:28px"></div>
  <div class="field abs" style="left:712px;top:814px;width:178px;height:68px"></div>
  <div class="btn-dark abs" style="left:751px;top:893px;width:107px;height:24px">Submit</div>

  <footer>
    <nav class="footer-nav abs">
      <span class="nav-link" style="left:192px">Home</span>
      <span class="nav-link" style="left:329px">Services</span>
      <span class="nav-link" style="left:479px">Support</span>
      <span class="nav-link" style="left:605px">Blog</span>
      <span class="nav-link" style="left:729px">Contact</span>
    </nav>
    <p class="copyright abs centered">Copyright © 2011. www.larchsystems.com</p>
  </footer>

</div>
</body>
</html>
```